Produktbilder für LED-Birnen
Zielgruppe
Wir verkaufen LED Birnen.
Hallo Liebe Designer,
wir wollen unsere Produktbilder etwas umgestallten. Bitte schaut euch dazu die angehängten Bilder an. Generell sollen die neuen Grafiken auf den Produktbildern absolut exklusiv wirken und auf schwarzem und weißen Hintergrund funktionieren. Gerne dürft ihr zuerst einmal Bild1 designen um von uns eine Bewertung zu erhalten.
Wir brauchen die PSD mit allen Schriften usw., sodass wir später selbständig Abmessungen etc. ändern können.
Lampe7: Das sind unser Produktbilder, die als Vorlage dienen sollen. Der Störer '3x' soll später auch noch zu finden sein, darf aber auch verschoben werden.
Bild1: Das wird das Hauptbild werden. Neben den Symbolen auf dem Beispielbild soll hier auch 'Helmlicht Werke' mit einer kleinen Deutschlandflagge zu seihen sein
Bild2: Soll die Abmessungen der Lampe enthalten aber natürlich schicker gestaltet sein
Bild3: Soll den Inhalt enthalten, darf aber gerne mit anderen Symbolen umgesetzt werden.
Bild4: Muss auch die Daten enthalten soll aber wesentlich schöner gestaltet werden.
Viele Spaß beim designen!

```html
<!DOCTYPE html>
<html lang="de">
<head>
<meta charset="utf-8">
<title>LED-Birnen – Produktbilder</title>
<link href="https://fonts.googleapis.com/css2?family=Montserrat:wght@300;400;500&family=Open+Sans:wght@400;600;700&display=swap" rel="stylesheet">
<style>
:root{
  --white:#ffffff;
  --black:#000000;
  --ink:#3a3a3a;
  --grey:#8a8a8a;
  --line:#555555;
}
*{margin:0;padding:0;box-sizing:border-box}
html,body{width:1200px;height:3000px;overflow:hidden;background:var(--white)}
.canvas{position:relative;width:1200px;height:3000px;overflow:hidden;font-family:"Open Sans",sans-serif;color:var(--ink)}
.abs{position:absolute}

.panel-dark{position:absolute;left:0;top:1750px;width:1200px;height:822px;background:var(--black)}

/* brand line */
.brand{position:absolute;left:40px;display:flex;align-items:center;gap:12px;
  font-family:"Montserrat",sans-serif;font-weight:400;font-size:21px;color:var(--ink);white-space:nowrap}
.brand .mark{width:14px;height:14px;background:currentColor;flex:none}
.brand.on-dark{color:var(--white);font-size:22px}

/* product photo areas */
.bulb-photo{position:absolute}
.bulb-edison{left:280px;top:268px;width:186px;height:408px;
  background:radial-gradient(ellipse at 50% 40%,#fff3d8 0,#f1c98b 35%,#d9a760 62%,#e8dccb 80%,#b08a2e 100%);
  border-radius:48% 48% 30% 30%/36% 36% 18% 18%}
.bulb-globe{left:233px;top:1089px;width:285px;height:437px;
  background:radial-gradient(ellipse at 50% 32%,#ffe7a8 0,#e8a24c 22%,#b8732e 42%,#8c5a2c 58%,#d6cfc6 72%,#2b2b2b 100%);
  border-radius:50% 50% 22% 22%/40% 40% 14% 14%}
.bulb-globe-dark{left:239px;top:1940px;width:279px;height:431px;
  background:radial-gradient(ellipse at 50% 30%,#ffe2a0 0,#e6983f 20%,#8e5423 40%,#4a2b12 58%,#1c1a18 76%,#000 100%);
  border-radius:50% 50% 22% 22%/40% 40% 14% 14%}
.shadow{position:absolute;left:250px;top:1545px;width:250px;height:24px;border-radius:50%;
  background:radial-gradient(ellipse,rgba(0,0,0,.28),rgba(0,0,0,0) 70%)}

.dim{position:absolute;font-family:"Montserrat",sans-serif;font-weight:300;font-size:11px;color:var(--grey);white-space:nowrap}
.dim.big{font-size:13px}
.dim.on-dark{color:var(--white)}
.dim.vertical{transform:rotate(-90deg);transform-origin:left top}

.icon{position:absolute;color:var(--line)}
.icon.on-dark{color:var(--white)}

/* lighting facts */
.facts{position:absolute;width:137px;height:196px;border:2px solid #777;border-radius:7px;padding:6px 6px 4px;
  font-size:7.2px;line-height:1.3;color:#555;background:var(--white)}
.facts .row{display:flex;justify-content:space-between}
.facts .title{font-weight:700;font-size:10px;color:#555}
.facts .title small{font-size:7.5px;font-weight:600}
.facts .rule{border-top:1px solid #999;margin:2px 0}
.facts .rule.thick{border-top:3px solid #777}
.facts b{font-weight:700}
.facts .scale{position:relative;height:14px;margin:1px 2px}
.facts .scale i{position:absolute;left:0;right:0;top:6px;border-top:1px solid #777}
.facts .scale em{position:absolute;top:3px;height:6px;border-left:1px solid #777}
.facts.dark{background:var(--black);border-color:var(--white);color:var(--white);transform:scale(1.085);transform-origin:left top}
.facts.dark .title{color:var(--white)}
.facts.dark .rule{border-color:var(--white)}
.facts.dark .scale i,.facts.dark .scale em{border-color:var(--white)}

.energy{position:absolute;width:137px;height:197px}

.multi-badge{position:absolute;left:14px;top:2324px;width:98px;height:97px;background:var(--white);border-radius:49px 49px 0 49px;
  font-family:"Montserrat",sans-serif;color:var(--black);display:flex;align-items:baseline;justify-content:center;padding-top:14px}
.multi-badge .num{font-size:52px;font-weight:300;line-height:1}
.multi-badge .x{font-size:22px;font-weight:300;margin-left:3px}

.temp-bar{position:absolute;
  background:linear-gradient(90deg,#7cc8ef 0,#9ed6f3 14%,#c2e5f6 28%,#e8f4fa 40%,#ffffff 48%,#fdf6c8 56%,#f8ea7d 66%,#f4cf35 78%,#f4a13a 84%,#f07a2c 92%,#ec5a25 100%)}
.temp-bar .k{position:absolute;top:50%;font-family:"Montserrat",sans-serif;font-size:9px;color:var(--white);transform:translate(-50%,-50%) rotate(-90deg)}

.grid-label{font-family:"Montserrat",sans-serif;font-weight:300;fill:#777}
</style>
</head>
<body>
<div class="canvas">

<svg width="0" height="0" style="position:absolute" aria-hidden="true">
  <defs>
    <linearGradient id="dimGrad" x1="0" x2="1">
      <stop offset="0" stop-color="currentColor" stop-opacity=".25"/>
      <stop offset="1" stop-color="currentColor"/>
    </linearGradient>
    <symbol id="sun" viewBox="0 0 60 60">
      <g stroke-width="2.6" stroke-linecap="round">
        <line x1="30" y1="8" x2="30" y2="15" stroke="#8fd3f4" transform="rotate(210 30 30)"/>
        <line x1="30" y1="8" x2="30" y2="15" stroke="#a9dcf5" transform="rotate(235 30 30)"/>
        <line x1="30" y1="8" x2="30" y2="15" stroke="#c6e8f7" transform="rotate(260 30 30)"/>
        <line x1="30" y1="8" x2="30" y2="15" stroke="#d5ecf7" transform="rotate(285 30 30)"/>
        <line x1="30" y1="8" x2="30" y2="15" stroke="#e6f2f8" transform="rotate(310 30 30)"/>
        <line x1="30" y1="8" x2="30" y2="15" stroke="#eef0dc" transform="rotate(335 30 30)"/>
        <line x1="30" y1="8" x2="30" y2="15" stroke="#f6e98f" transform="rotate(0 30 30)"/>
        <line x1="30" y1="8" x2="30" y2="15" stroke="#f6dc4a" transform="rotate(25 30 30)"/>
        <line x1="30" y1="8" x2="30" y2="15" stroke="#f5c23a" transform="rotate(50 30 30)"/>
        <line x1="30" y1="8" x2="30" y2="15" stroke="#f4a332" transform="rotate(75 30 30)"/>
        <line x1="30" y1="8" x2="30" y2="15" stroke="#f2832c" transform="rotate(100 30 30)"/>
        <line x1="30" y1="8" x2="30" y2="15" stroke="#ef6128" transform="rotate(125 30 30)"/>
        <line x1="30" y1="8" x2="30" y2="15" stroke="#ec4a26" transform="rotate(150 30 30)"/>
      </g>
      <path d="M24 55 l3 -5 l3 5z" fill="currentColor"/>
    </symbol>
    <symbol id="bulb" viewBox="0 0 60 60">
      <g fill="none" stroke="currentColor" stroke-width="1.4" stroke-linecap="round">
        <circle cx="30" cy="27" r="10"/>
        <path d="M25 37 v3 h10 v-3 M25.5 42.5 h9 M26.5 45 h7"/>
        <g stroke-width="1.6">
          <line x1="30" y1="13" x2="30" y2="8"/>
          <line x1="30" y1="13" x2="30" y2="8" transform="rotate(-30 30 27)"/>
          <line x1="30" y1="13" x2="30" y2="8" transform="rotate(30 30 27)"/>
          <line x1="30" y1="13" x2="30" y2="8" transform="rotate(-60 30 27)"/>
          <line x1="30" y1="13" x2="30" y2="8" transform="rotate(60 30 27)"/>
          <line x1="30" y1="13" x2="30" y2="8" transform="rotate(-90 30 27)"/>
          <line x1="30" y1="13" x2="30" y2="8" transform="rotate(90 30 27)"/>
          <line x1="30" y1="13" x2="30" y2="8" transform="rotate(-115 30 27)"/>
          <line x1="30" y1="13" x2="30" y2="8" transform="rotate(115 30 27)"/>
        </g>
      </g>
    </symbol>
    <symbol id="dim" viewBox="0 0 60 60">
      <path d="M15 37 A15 15 0 0 1 45 37" fill="none" stroke="url(#dimGrad)" stroke-width="4.5"/>
      <path d="M12 41 h4 M43 41 h4 M45 39 v4" stroke="currentColor" stroke-width="1"/>
      <text x="30" y="48" text-anchor="middle" font-family="Open Sans,sans-serif" font-size="5" fill="currentColor">Dimmable</text>
    </symbol>
    <symbol id="tick" viewBox="0 0 60 60">
      <path d="M21 29 l6 6 l12 -14" fill="none" stroke="currentColor" stroke-width="2.6" stroke-linecap="round" stroke-linejoin="round"/>
    </symbol>
    <symbol id="energy-label" viewBox="0 0 137 197">
      <g font-family="Open Sans,sans-serif" font-weight="700" font-size="10" fill="#fff">
        <path d="M8 50 h30 l6 6 l-6 6 h-30z" fill="#009a44"/><text x="11" y="60">A<tspan font-size="6" dy="-4">+++</tspan></text>
        <path d="M8 66 h36 l6 6 l-6 6 h-36z" fill="#3bab3c"/><text x="11" y="76">A<tspan font-size="6" dy="-4">++</tspan></text>
        <path d="M8 82 h42 l6 6 l-6 6 h-42z" fill="#8cc63e"/><text x="11" y="92">A<tspan font-size="6" dy="-4">+</tspan></text>
        <path d="M8 98 h48 l6 6 l-6 6 h-48z" fill="#f1e400"/><text x="11" y="108">A</text>
        <path d="M8 114 h54 l6 6 l-6 6 h-54z" fill="#fbb916"/><text x="11" y="124">B</text>
        <path d="M8 130 h60 l6 6 l-6 6 h-60z" fill="#f37021"/><text x="11" y="140">C</text>
        <path d="M8 146 h66 l6 6 l-6 6 h-66z" fill="#e3101b"/><text x="11" y="156">D</text>
      </g>
    </symbol>
  </defs>
</svg>

<!-- ============ dimensions ============ -->
<div class="brand" style="top:94px"><span class="mark"></span>Helmlicht Werke</div>

<div class="bulb-photo bulb-edison" role="img" aria-label="Amberfarbene Edison-Filament-LED-Birne ST64 mit spiralförmigem Glühfaden und E27-Sockel"></div>

<svg class="abs" style="left:0;top:0" width="520" height="720" aria-hidden="true">
  <g stroke="#555" stroke-width="1">
    <line x1="227" y1="272" x2="227" y2="666"/>
    <path d="M223 276 L227 268 L231 276z M223 662 L227 670 L231 662z" fill="#555"/>
    <line x1="284" y1="702" x2="470" y2="702"/>
    <path d="M288 698 L280 702 L288 706z M466 698 L474 702 L466 706z" fill="#555"/>
  </g>
</svg>
<div class="dim vertical" style="left:207px;top:516px">140 mm = 5.51 in</div>
<div class="dim" style="left:338px;top:705px">64 mm = 2.52 in</div>

<svg class="icon" style="left:718px;top:272px" width="64" height="64" viewBox="0 0 60 60" role="img" aria-label="Farbtemperatur 2200K"><use href="#sun"/><text x="33" y="55" font-size="4" fill="#888" font-family="Montserrat,sans-serif">2200K</text></svg>
<svg class="icon" style="left:716px;top:358px" width="68" height="68" viewBox="0 0 60 60" role="img" aria-label="Farbwiedergabe 90+"><use href="#bulb"/><text x="30" y="29" text-anchor="middle" font-size="6" fill="#555" font-family="Open Sans,sans-serif">90+</text></svg>
<svg class="icon" style="left:722px;top:449px" width="58" height="58" viewBox="0 0 60 60" role="img" aria-label="Konformitätszeichen"><circle cx="30" cy="30" r="27" fill="none" stroke="currentColor" stroke-width="2.5"/><use href="#tick"/></svg>
<svg class="icon" style="left:722px;top:535px" width="58" height="58" viewBox="0 0 60 60" role="img" aria-label="Dimmbar"><circle cx="30" cy="30" r="27" fill="none" stroke="currentColor" stroke-width="2.5"/><use href="#dim"/></svg>
<svg class="icon" style="left:722px;top:620px" width="58" height="58" viewBox="0 0 60 60" role="img" aria-label="Prüfzeichen"><circle cx="30" cy="30" r="27" fill="none" stroke="currentColor" stroke-width="2.5"/></svg>

<div class="facts" style="left:824px;top:268px">
  <div class="row title"><span>Lighting Facts</span><small>Per Bulb</small></div>
  <div class="rule thick"></div>
  <div class="row"><b>Brightness</b><span>180 lumens</span></div>
  <div class="rule"></div>
  <div><b>Estimated Yearly Energy Cost</b><br><b>$0.48</b><br>Based on 3 hrs/day, 11¢/kWh<br>Cost depends on rates and use</div>
  <div class="rule"></div>
  <div><b>Life</b></div>
  <div class="row"><span>Based on 3 hrs/day</span><b>14 years</b></div>
  <div class="rule"></div>
  <div><b>Light Appearance</b></div>
  <div class="row"><span>warm</span><span>cool</span></div>
  <div class="scale"><i></i><em style="left:0"></em><em style="left:33%"></em><em style="left:66%"></em><em style="right:0"></em></div>
  <div style="margin-left:8px">2200K</div>
  <div class="rule"></div>
  <div class="row"><b>Energy Used</b><b>4 watts</b></div>
</div>

<svg class="energy" style="left:824px;top:482px" viewBox="0 0 137 197" role="img" aria-label="Energieeffizienzklasse A++, 4 kWh pro 1000 Stunden">
  <rect x="1.5" y="1.5" width="134" height="194" rx="7" fill="#fff" stroke="#777" stroke-width="2.5"/>
  <rect x="8" y="10" width="32" height="20" fill="#666"/>
  <text x="48" y="24" font-family="Open Sans,sans-serif" font-weight="400" font-size="11" fill="#666">Energy class</text>
  <use href="#energy-label"/>
  <path d="M94 72 l7 -7 h27 v14 h-27z" fill="#333"/><text x="106" y="76" font-family="Open Sans,sans-serif" font-weight="700" font-size="9" fill="#fff">A<tspan font-size="6" dy="-3">++</tspan></text>
  <text x="70" y="184" text-anchor="middle" font-family="Open Sans,sans-serif" font-weight="700" font-size="9" fill="#555">4kWh/1000h</text>
</svg>

<!-- ============ features ============ -->
<div class="brand" style="top:884px"><span class="mark"></span>Helmlicht Werke</div>

<svg class="abs" style="left:0;top:960px" width="720" height="700" aria-hidden="true">
  <path d="M207 438 A235 235 0 1 1 610 275" fill="none" stroke="#555" stroke-width="1.6"/>
  <line x1="239" y1="622" x2="517" y2="622" stroke="#555" stroke-width="1.2"/>
  <circle cx="239" cy="622" r="3.5" fill="#555"/><circle cx="517" cy="622" r="3.5" fill="#555"/>
</svg>

<div class="bulb-photo bulb-globe" role="img" aria-label="Amberfarbene Globe-Filament-LED-Birne G80 mit leuchtenden Glühfäden und E27-Sockel"></div>
<div class="shadow" aria-hidden="true"></div>
<div class="dim big" style="left:332px;top:1585px">64 mm = 2.52 in</div>

<svg class="icon" style="left:278px;top:973px" width="68" height="68" viewBox="0 0 60 60" role="img" aria-label="Konformitätszeichen"><circle cx="30" cy="30" r="28" fill="#fff" stroke="currentColor" stroke-width="1.6"/></svg>
<svg class="icon" style="left:504px;top:1033px" width="68" height="68" viewBox="0 0 60 60" role="img" aria-label="Dimmbar"><circle cx="30" cy="30" r="28" fill="#fff" stroke="currentColor" stroke-width="1.6"/><use href="#dim"/></svg>
<svg class="icon" style="left:113px;top:1138px" width="68" height="68" viewBox="0 0 60 60" role="img" aria-label="Farbwiedergabe 90"><circle cx="30" cy="30" r="28" fill="#fff" stroke="currentColor" stroke-width="1.6"/><use href="#bulb" x="-6" y="0" width="60" height="60"/><text x="35" y="38" font-size="12" font-family="Montserrat,sans-serif" fill="#555">90</text></svg>
<svg class="icon" style="left:566px;top:1260px" width="68" height="68" viewBox="0 0 60 60" role="img" aria-label="Prüfzeichen"><circle cx="30" cy="30" r="28" fill="#fff" stroke="currentColor" stroke-width="1.6"/><use href="#tick"/></svg>
<svg class="icon" style="left:173px;top:1364px" width="68" height="68" viewBox="0 0 60 60" role="img" aria-label="Farbtemperatur 2200K"><circle cx="30" cy="30" r="28" fill="#fff" stroke="currentColor" stroke-width="1.6"/><use href="#sun" x="9" y="9" width="42" height="42"/></svg>

<div class="facts" style="left:824px;top:1092px">
  <div class="row title"><span>Lighting Facts</span><small>Per Bulb</small></div>
  <div class="rule thick"></div>
  <div class="row"><b>Brightness</b><span>180 lumens</span></div>
  <div class="rule"></div>
  <div><b>Estimated Yearly Energy Cost</b><br><b>$0.48</b><br>Based on 3 hrs/day, 11¢/kWh<br>Cost depends on rates and use</div>
  <div class="rule"></div>
  <div><b>Life</b></div>
  <div class="row"><span>Based on 3 hrs/day</span><b>14 years</b></div>
  <div class="rule"></div>
  <div><b>Light Appearance</b></div>
  <div class="row"><span>warm</span><span>cool</span></div>
  <div class="scale"><i></i><em style="left:0"></em><em style="left:33%"></em><em style="left:66%"></em><em style="right:0"></em></div>
  <div style="margin-left:8px">2200K</div>
  <div class="rule"></div>
  <div class="row"><b>Energy Used</b><b>4 watts</b></div>
</div>

<svg class="energy" style="left:824px;top:1306px" viewBox="0 0 137 197" role="img" aria-label="Energieeffizienzklasse A++, 4 kWh pro 1000 Stunden">
  <rect x="1.5" y="1.5" width="134" height="194" rx="7" fill="#fff" stroke="#777" stroke-width="2.5"/>
  <rect x="8" y="10" width="32" height="20" fill="#666"/>
  <text x="48" y="24" font-family="Open Sans,sans-serif" font-weight="400" font-size="11" fill="#666">Energy class</text>
  <use href="#energy-label"/>
  <path d="M94 72 l7 -7 h27 v14 h-27z" fill="#333"/><text x="106" y="76" font-family="Open Sans,sans-serif" font-weight="700" font-size="9" fill="#fff">A<tspan font-size="6" dy="-3">++</tspan></text>
  <text x="70" y="184" text-anchor="middle" font-family="Open Sans,sans-serif" font-weight="700" font-size="9" fill="#555">4kWh/1000h</text>
</svg>

<!-- ============ main image on black ============ -->
<div class="panel-dark"></div>

<div class="brand on-dark" style="top:1784px"><span class="mark"></span>Helmlicht Werke</div>

<div class="bulb-photo bulb-globe-dark" role="img" aria-label="Leuchtende Globe-Filament-LED-Birne mit warmem Licht vor schwarzem Hintergrund"></div>

<svg class="abs" style="left:0;top:1930px" width="560" height="490" aria-hidden="true">
  <g stroke="#fff" stroke-width="1.2" fill="none">
    <path d="M196 12 H189 V447 H196"/>
    <path d="M242 474 V482 H521 V474"/>
  </g>
</svg>
<div class="dim on-dark vertical" style="left:166px;top:2202px">140 mm = 5.51 in</div>
<div class="dim big on-dark" style="left:335px;top:2424px">64 mm = 2.52 in</div>

<div class="multi-badge"><span class="num">3</span><span class="x">x</span></div>

<div class="facts dark" style="left:725px;top:2014px">
  <div class="row title"><span>Lighting Facts</span><small>Per Bulb</small></div>
  <div class="rule thick"></div>
  <div class="row"><b>Brightness</b><span>180 lumens</span></div>
  <div class="rule"></div>
  <div><b>Estimated Yearly Energy Cost</b><br><b>$0.48</b><br>Based on 3 hrs/day, 11¢/kWh<br>Cost depends on rates and use</div>
  <div class="rule"></div>
  <div><b>Life</b></div>
  <div class="row"><span>Based on 3 hrs/day</span><b>14 years</b></div>
  <div class="rule"></div>
  <div><b>Light Appearance</b></div>
  <div class="row"><span>warm</span><span>cool</span></div>
  <div class="scale"><i></i><em style="left:0"></em><em style="left:33%"></em><em style="left:66%"></em><em style="right:0"></em></div>
  <div style="margin-left:8px">2200K</div>
  <div class="rule"></div>
  <div class="row"><b>Energy Used</b><b>4 watts</b></div>
</div>

<svg class="energy" style="left:894px;top:2014px;width:150px;height:216px" viewBox="0 0 137 197" role="img" aria-label="Energieeffizienzklasse A++, 4 kWh pro 1000 Stunden">
  <rect x="1.5" y="1.5" width="134" height="194" rx="7" fill="#000" stroke="#fff" stroke-width="2.5"/>
  <rect x="8" y="10" width="32" height="20" fill="#fff"/>
  <text x="48" y="24" font-family="Open Sans,sans-serif" font-weight="400" font-size="11" fill="#fff">Energy class</text>
  <use href="#energy-label"/>
  <path d="M94 72 l7 -7 h27 v14 h-27z" fill="#fff"/><text x="106" y="76" font-family="Open Sans,sans-serif" font-weight="700" font-size="9" fill="#000">A<tspan font-size="6" dy="-3">++</tspan></text>
  <text x="70" y="184" text-anchor="middle" font-family="Open Sans,sans-serif" font-weight="700" font-size="9" fill="#fff">4kWh/1000h</text>
</svg>

<svg class="icon on-dark" style="left:733px;top:2264px" width="63" height="63" viewBox="0 0 60 60" role="img" aria-label="Farbwiedergabe 80+"><rect x="1.5" y="1.5" width="57" height="57" rx="8" fill="none" stroke="currentColor" stroke-width="1.6"/><use href="#bulb"/><text x="30" y="29" text-anchor="middle" font-size="6" fill="#fff" font-family="Open Sans,sans-serif">80+</text></svg>
<svg class="icon on-dark" style="left:812px;top:2264px" width="63" height="63" viewBox="0 0 60 60" role="img" aria-label="Konformitätszeichen"><rect x="1.5" y="1.5" width="57" height="57" rx="8" fill="none" stroke="currentColor" stroke-width="1.6"/></svg>
<svg class="icon on-dark" style="left:891px;top:2264px" width="63" height="63" viewBox="0 0 60 60" role="img" aria-label="Dimmbar"><rect x="1.5" y="1.5" width="57" height="57" rx="8" fill="none" stroke="currentColor" stroke-width="1.6"/><use href="#dim"/></svg>
<svg class="icon on-dark" style="left:972px;top:2264px" width="63" height="63" viewBox="0 0 60 60" role="img" aria-label="Prüfzeichen"><rect x="1.5" y="1.5" width="57" height="57" rx="8" fill="none" stroke="currentColor" stroke-width="1.6"/><use href="#tick"/></svg>

<div class="temp-bar" style="left:722px;top:2365px;width:323px;height:47px"><span class="k" style="left:251px">2200K</span></div>

<!-- ============ icon set ============ -->
<svg class="abs" style="left:55px;top:2635px" width="270" height="290" viewBox="0 0 270 290" role="img" aria-label="Symbolvarianten Farbwiedergabe 90, 80 und 70">
  <g color="#777">
    <use href="#bulb" x="14" y="0" width="60" height="60"/>
    <use href="#bulb" x="99" y="0" width="60" height="60"/>
    <use href="#bulb" x="183" y="0" width="60" height="60"/>
    <text x="44" y="30" text-anchor="middle" class="grid-label" font-size="8">90+</text>
    <text x="129" y="30" text-anchor="middle" class="grid-label" font-size="8">80+</text>
    <text x="213" y="30" text-anchor="middle" class="grid-label" font-size="8">70+</text>

    <use href="#bulb" x="4" y="82" width="60" height="60"/>
    <use href="#bulb" x="89" y="82" width="60" height="60"/>
    <use href="#bulb" x="173" y="82" width="60" height="60"/>
    <text x="51" y="124" class="grid-label" font-size="20">90</text>
    <text x="136" y="124" class="grid-label" font-size="20">80</text>
    <text x="220" y="124" class="grid-label" font-size="20">70</text>

    <g fill="none" stroke="currentColor" stroke-width="1.4">
      <path d="M34 196 l10 -16 h19 l10 16 l-10 16 h-19z" transform="translate(-10 0)"/>
      <path d="M34 196 l10 -16 h19 l10 16 l-10 16 h-19z" transform="translate(75 0)"/>
      <path d="M34 196 l10 -16 h19 l10 16 l-10 16 h-19z" transform="translate(160 0)"/>
      <g stroke-linecap="round">
        <path d="M33 175 l-4 -5 M74 175 l4 -5 M43 169 l-2 -6 M63 169 l2 -6 M53 167 v-6 M27 190 h-6 M81 190 h6" transform="translate(-10 0)"/>
        <path d="M33 175 l-4 -5 M74 175 l4 -5 M43 169 l-2 -6 M63 169 l2 -6 M53 167 v-6 M27 190 h-6 M81 190 h6" transform="translate(75 0)"/>
        <path d="M33 175 l-4 -5 M74 175 l4 -5 M43 169 l-2 -6 M63 169 l2 -6 M53 167 v-6 M27 190 h-6 M81 190 h6" transform="translate(160 0)"/>
      </g>
      <path d="M38 214 h12 v5 l-6 5 l-6 -5z M123 214 h12 v5 l-6 5 l-6 -5z M208 214 h12 v5 l-6 5 l-6 -5z"/>
    </g>
    <text x="44" y="256" text-anchor="middle" class="grid-label" font-size="20">90<tspan font-size="10" dy="-9">+</tspan></text>
    <text x="129" y="256" text-anchor="middle" class="grid-label" font-size="20">80<tspan font-size="10" dy="-9">+</tspan></text>
    <text x="214" y="256" text-anchor="middle" class="grid-label" font-size="20">70<tspan font-size="10" dy="-9">+</tspan></text>
  </g>
</svg>

<svg class="abs" style="left:412px;top:2630px;color:#777" width="160" height="170" viewBox="0 0 60 64" role="img" aria-label="Farbtemperatur 2200K">
  <use href="#sun"/>
  <text x="33" y="55" font-family="Montserrat,sans-serif" font-size="4" fill="#888">2200K</text>
</svg>

<div class="temp-bar" style="left:362px;top:2845px;width:272px;height:41px"><span class="k" style="left:212px">2200K</span></div>

<svg class="icon" style="left:670px;top:2666px" width="72" height="72" viewBox="0 0 60 60" role="img" aria-label="Farbtemperatur"><circle cx="30" cy="30" r="28" fill="none" stroke="currentColor" stroke-width="1.4"/><use href="#sun" x="9" y="9" width="42" height="42"/></svg>
<svg class="icon" style="left:770px;top:2666px" width="72" height="72" viewBox="0 0 60 60" role="img" aria-label="Farbwiedergabe 90"><circle cx="30" cy="30" r="28" fill="none" stroke="currentColor" stroke-width="1.4"/><use href="#bulb" x="-6"/><text x="35" y="38" font-size="12" font-family="Montserrat,sans-serif" fill="#555">90</text></svg>
<svg class="icon" style="left:870px;top:2666px" width="72" height="72" viewBox="0 0 60 60" role="img" aria-label="Konformitätszeichen"><circle cx="30" cy="30" r="28" fill="none" stroke="currentColor" stroke-width="1.4"/></svg>
<svg class="icon" style="left:971px;top:2666px" width="72" height="72" viewBox="0 0 60 60" role="img" aria-label="Dimmbar"><circle cx="30" cy="30" r="28" fill="none" stroke="currentColor" stroke-width="1.4"/><use href="#dim"/></svg>
<svg class="icon" style="left:1070px;top:2666px" width="72" height="72" viewBox="0 0 60 60" role="img" aria-label="Prüfzeichen"><circle cx="30" cy="30" r="28" fill="none" stroke="currentColor" stroke-width="1.4"/><use href="#tick"/></svg>

<svg class="icon" style="left:711px;top:2808px" width="77" height="77" viewBox="0 0 60 60" role="img" aria-label="Farbwiedergabe 80+"><rect x="1.5" y="1.5" width="57" height="57" rx="8" fill="none" stroke="currentColor" stroke-width="1.3"/><use href="#bulb"/><text x="30" y="29" text-anchor="middle" font-size="6" fill="#555" font-family="Open Sans,sans-serif">80+</text></svg>
<svg class="icon" style="left:810px;top:2808px" width="77" height="77" viewBox="0 0 60 60" role="img" aria-label="Konformitätszeichen"><rect x="1.5" y="1.5" width="57" height="57" rx="8" fill="none" stroke="currentColor" stroke-width="1.3"/></svg>
<svg class="icon" style="left:908px;top:2808px" width="77" height="77" viewBox="0 0 60 60" role="img" aria-label="Dimmbar"><rect x="1.5" y="1.5" width="57" height="57" rx="8" fill="none" stroke="currentColor" stroke-width="1.3"/><use href="#dim"/></svg>
<svg class="icon" style="left:1006px;top:2808px" width="77" height="77" viewBox="0 0 60 60" role="img" aria-label="Prüfzeichen"><rect x="1.5" y="1.5" width="57" height="57" rx="8" fill="none" stroke="currentColor" stroke-width="1.3"/><use href="#tick"/></svg>

</div>
</body>
</html>
```